Business cards for landscaping company
Torvend Landscaping, LLC
Business cards for landscaping company - Construction
Creative Brief
Professional
Wesley R. Torvend
Owner
47 Birchell Lane Palmer, MA 01082
torvendlandscaping@quillmail.example
Landscape Design/ Excavation Paver Walkways/ Patios Hydroseeding New lawn installations Commercial Property Maintenance Custom Outdoor Living Areas Snow and Ice Management

```html
<!DOCTYPE html>
<html lang="en">
<head>
<meta charset="utf-8">
<title>Torvend Landscaping, LLC – Business Cards</title>
<link rel="stylesheet" href="https://fonts.googleapis.com/css2?family=Questrial&display=swap">
<style>
  :root {
    --page-bg: #1c1c1e;
    --card-black: #0b0b0c;
    --card-sheen: #1f1f22;
    --text-light: #e6e6e6;
    --text-muted: #c9c9c9;
    --text-dark: #1a1a1a;
    --silver-top: #f2f2f2;
    --silver-mid: #b9bcc0;
    --silver-low: #7c8086;
    --stripe-light: #bfc2c6;
    --stripe-dark: #3a3b3e;
  }
  * { box-sizing: border-box; margin: 0; padding: 0; }
  html, body { width: 1200px; height: 626px; overflow: hidden; }
  body {
    background: var(--page-bg);
    font-family: "Questrial", "Century Gothic", sans-serif;
    display: flex;
    align-items: center;
    justify-content: center;
    gap: 40px;
  }
  .card {
    position: relative;
    width: 540px;
    height: 309px;
    border-radius: 18px;
    overflow: hidden;
    background: linear-gradient(160deg, var(--card-sheen) 0%, var(--card-black) 45%, var(--card-black) 100%);
    box-shadow: 0 10px 30px rgba(0,0,0,.5);
  }
  .stripe-tab {
    position: absolute;
    border-radius: 10px;
    background: linear-gradient(135deg, var(--stripe-light), var(--stripe-dark));
    opacity: .8;
  }

  /* Front */
  .silver-panel { position: absolute; inset: 0; width: 100%; height: 100%; }
  .owner-block {
    position: absolute;
    top: 52px;
    left: 160px;
    width: 196px;
    text-align: right;
    color: var(--text-dark);
  }
  .owner-name { font-size: 23px; letter-spacing: .2px; white-space: nowrap; }
  .owner-title { font-size: 15px; margin-top: 2px; }
  .front .stripe-tab.top-right { top: 42px; right: -10px; width: 72px; height: 48px; }
  .contact-block {
    position: absolute;
    left: 340px;
    right: 14px;
    bottom: 40px;
    color: var(--text-muted);
    font-size: 13px;
    line-height: 1.45;
  }
  .contact-block .gap { height: 14px; }
  .contact-email { font-size: 11px; white-space: nowrap; }

  /* Back */
  .back .stripe-tab.left-top { top: 40px; left: -10px; width: 48px; height: 80px; }
  .back .stripe-tab.left-bottom { bottom: 24px; left: -10px; width: 48px; height: 70px; }
  .back .stripe-tab.right-bottom { bottom: 24px; right: -10px; width: 60px; height: 40px; }
  .services {
    position: absolute;
    top: 50%;
    right: 190px;
    transform: translateY(-50%);
    list-style: none;
    text-align: right;
    color: var(--text-light);
    font-size: 15px;
    line-height: 1.4;
  }
  .company-name {
    position: absolute;
    right: 28px;
    top: 30px;
    color: var(--text-light);
    font-size: 14px;
  }
</style>
</head>
<body>

  <section class="card front" aria-label="Business card front">
    <svg class="silver-panel" viewBox="0 0 540 309" aria-hidden="true">
      <defs>
        <linearGradient id="silverFill" x1="0" y1="0" x2="0.3" y2="1">
          <stop offset="0" stop-color="#f2f2f2"/>
          <stop offset=".45" stop-color="#b9bcc0"/>
          <stop offset="1" stop-color="#7c8086"/>
        </linearGradient>
      </defs>
      <path d="M190 0 H372 L306 309 H196 L152 48 Q146 0 190 0 Z" fill="url(#silverFill)"/>
    </svg>
    <div class="stripe-tab top-right" role="img" aria-label="Diagonal silver stripe accent"></div>
    <div class="owner-block">
      <p class="owner-name">Wesley R. Torvend</p>
      <p class="owner-title">Owner</p>
    </div>
    <div class="contact-block">
      <p>47 Birchell Lane</p>
      <p>Palmer, MA 01082</p>
      <div class="gap"></div>
      <p class="contact-email">torvendlandscaping@quillmail.example</p>
      <p>(413) 555-0147</p>
    </div>
  </section>

  <section class="card back" aria-label="Business card back">
    <div class="stripe-tab left-top" role="img" aria-label="Diagonal silver stripe accent"></div>
    <div class="stripe-tab left-bottom" role="img" aria-label="Diagonal silver stripe accent"></div>
    <div class="stripe-tab right-bottom" role="img" aria-label="Diagonal silver stripe accent"></div>
    <p class="company-name">Torvend Landscaping, LLC</p>
    <ul class="services">
      <li>Landscape Design/ Excavation</li>
      <li>Paver Walkways/ Patios</li>
      <li>Hydroseeding</li>
      <li>New lawn installations</li>
      <li>Commercial Property Maintenance</li>
      <li>Custom Outdoor Living Areas</li>
      <li>Snow and Ice Management</li>
    </ul>
  </section>

</body>
</html>
```